Curantel System Web Page Design

This project is to design 6 pages of a web based medical system for clinics, hospitals, drugs suppliers, general items suppliers, insurance company, laboratories and patients (basically all parties which could be involved in).We want the designs of the browser, button, icon and layout are based on Oru, which is user friendly, looks professional, simple and neat but with powerful functions. We have uploaded few pictures of another system, please do not copy its design because this is not what we are looking for, the pictures are for you to know the elements should be included in our pages. Curantel web-base system, design 6 pages1. Login PageShould include the following elements-company id with input field-login id with input field-password with input field2. Main Page (Navigation page)Should include the following elements-Appointment-Consultation-Patient-Drugs inventory -General supplies inventory -Laboratory-Suppliers-Insurance-Reports 3. Appointment PageShould include all the the elements in the respective pictures plus the followings-Daily View, Weekly View, Monthly View buttons4. Consultation PageShould include all the the elements in the respective picture5. Patient Page5.1 General information Should include all the the elements in the respective picture5.2 medical history/lab reportsShould include all the the elements in the respective picture plus the followings-Notify patient button-Share report button.
Please stop using Ward Harbor in your designs which is not the name of our system. We have just rename our system to Curantel, please take note.
We need the system to look professional not playful, do not use too many colors and playful icons.
professional users
5+ page

```html
<!DOCTYPE html>
<html lang="en">
<head>
<meta charset="utf-8">
<title>Curantel – Current Queue</title>
<link href="https://fonts.googleapis.com/css2?family=Inter:wght@300;400;500;600&display=swap" rel="stylesheet">
<style>
:root{
  --blue:#1a86ef;
  --blue-dark:#1570d6;
  --ink:#1f2329;
  --ink-soft:#3b4047;
  --label:#5b636d;
  --muted:#a9adb3;
  --line:#d3d7dc;
  --line-soft:#e2e5e8;
  --side-bg:#eceef1;
  --main-bg:#f8f9fa;
  --white:#ffffff;
  --red:#e8312f;
  --dot-a:#2f8cf0;
  --dot-b:#3cbf5a;
  --dot-c:#c66ad8;
}
*{box-sizing:border-box;margin:0;padding:0}
html,body{width:1200px;height:982px;overflow:hidden}
body{font-family:"Inter",sans-serif;color:var(--ink);background:var(--main-bg);position:relative}
.abs{position:absolute}

/* header */
.topbar{left:0;top:0;width:1200px;height:80px;background:var(--white);border-bottom:1px solid var(--line)}
.brand{left:29px;top:20px;font-size:30px;font-weight:400;color:var(--blue);letter-spacing:.2px}
.avatar{left:954px;top:12px;width:56px;height:56px;border-radius:50%;background:radial-gradient(circle at 50% 40%,#c9b7a6,#6d7f95 70%);border:1px solid var(--line)}
.user-name{left:1025px;top:30px;font-size:17px;color:var(--ink)}
.user-menu{left:1142px;top:33px}

/* sidebar */
.sidebar{left:0;top:81px;width:206px;height:901px;background:var(--side-bg);border-right:1px solid var(--line-soft)}
.nav-group{position:absolute;left:29px;font-size:16px;font-weight:600;color:var(--label)}
.nav-sub{position:absolute;left:29px;font-size:16px;font-weight:300;color:var(--ink)}
.nav-active{left:0;top:148px;width:206px;height:38px;background:var(--blue);color:var(--white);font-size:16px;font-weight:300;padding-left:29px;line-height:38px}
.nav-rule{position:absolute;left:0;width:206px;height:1px;background:#d7dadd}

/* labels & fields */
.label{font-size:16px;font-weight:600;color:var(--label)}
.field{background:var(--white);border:1px solid var(--line);border-radius:4px;font-size:16px;font-weight:300;color:var(--ink);padding-left:16px;display:flex;align-items:center}
.field svg{position:absolute;right:12px;top:50%;transform:translateY(-50%)}

/* patient card */
.patient-card{left:252px;top:199px;width:299px;height:153px;background:var(--white);border:1px solid var(--line);border-radius:4px;font-size:12px;font-weight:300;color:var(--ink-soft)}
.patient-card .row{height:30.6px;border-bottom:1px solid var(--line-soft);display:flex;align-items:center;justify-content:space-between;padding:0 15px}
.patient-card .row:last-child{border-bottom:none}

/* calendar */
.calendar{left:252px;top:370px;width:299px;height:197px;background:var(--white);border:1px solid var(--line);border-radius:4px}
.cal-title{left:32px;top:10px;font-size:22px;font-weight:500;color:var(--ink)}
.cal-title .year{color:var(--red);font-weight:400}
.cal-nav{top:20px}
.cal-grid{left:27px;top:44px;display:grid;grid-template-columns:24px repeat(7,31px);grid-auto-rows:20px;align-items:center;text-align:center}
.cal-head{font-size:8px;color:#6b7078;height:14px}
.cw{font-size:8px;color:#8a8f96;border-right:1px solid var(--line-soft);height:20px;line-height:20px}
.day{font-size:10px;font-weight:600;color:var(--ink);position:relative;line-height:16px}
.day::after{content:"";position:absolute;left:50%;top:15px;width:2.5px;height:2.5px;margin-left:-1px;border-radius:50%;background:var(--dot-b);box-shadow:-4px 0 var(--dot-a),4px 0 var(--dot-c)}
.day.next{font-weight:300;color:#8d9198}
.week-band{left:35px;top:123px;width:244px;height:18px;border-radius:9px;background:#eef0f2}
.cw.now{color:var(--blue)}
.day.today{color:var(--white)}
.day.today span{position:relative;z-index:1}
.day.today::before{content:"";position:absolute;left:50%;top:50%;width:24px;height:24px;margin:-12px 0 0 -12px;border-radius:50%;background:var(--blue)}
.day.today::after{background:var(--white);box-shadow:-4px 0 var(--white),4px 0 var(--white);top:17px;z-index:1}

.divider-v{left:600px;top:81px;width:1px;height:527px;background:var(--line-soft)}

/* queue table */
.queue{left:206px;top:608px;width:994px;height:206px;background:var(--white);border-top:1px solid var(--line-soft);border-bottom:1px solid var(--line)}
.queue-head{position:absolute;top:0;left:0;width:994px;height:35px;border-bottom:1px solid var(--line);background:var(--main-bg)}
.th{position:absolute;top:10px;font-size:16px;font-weight:600;color:var(--label)}
.tr{position:absolute;left:0;width:994px;height:31px;border-bottom:1px solid var(--line-soft);font-size:12px;font-weight:300;color:var(--ink-soft)}
.tr span{position:absolute;top:9px}
.tr.fade{border-bottom:none;color:#b9bdc2}
.scroll-thumb{left:1182px;top:700px;width:7px;height:89px;border-radius:4px;background:#a8abb0}

/* actions */
.btn{position:absolute;height:37px;border:1.5px solid var(--blue);border-radius:4px;background:var(--white);color:var(--blue);font-family:inherit;font-size:15px;font-weight:300;display:flex;align-items:center;justify-content:center}
.btn.off{border-color:var(--line);color:#c3c6ca}
</style>
</head>
<body>

<header class="abs topbar">
  <div class="abs brand">Curantel</div>
  <div class="abs avatar" role="img" aria-label="User profile photo"></div>
  <div class="abs user-name">Owen Marsh</div>
  <svg class="abs user-menu" width="18" height="12" viewBox="0 0 18 12"><path d="M2 2l7 7 7-7" fill="none" stroke="var(--blue)" stroke-width="2.6" stroke-linecap="round" stroke-linejoin="round"/></svg>
</header>

<nav class="abs sidebar">
  <div class="nav-group" style="top:29px">Appointments</div>
  <div class="abs nav-active" style="top:67px">Current Queue</div>
  <div class="nav-sub" style="top:115px">Daily View</div>
  <div class="nav-sub" style="top:154px">Weekly View</div>
  <div class="nav-sub" style="top:193px">Monthly View</div>
  <div class="nav-rule" style="top:239px"></div>
  <div class="nav-group" style="top:248px">Consultation</div>
  <div class="nav-rule" style="top:273px"></div>
  <div class="nav-group" style="top:280px">Patient</div>
  <div class="nav-rule" style="top:304px"></div>
  <div class="nav-group" style="top:311px">Drugs inventory</div>
  <div class="nav-rule" style="top:335px"></div>
  <div class="nav-group" style="top:342px;line-height:19px">General supplies<br>inventory</div>
  <div class="nav-rule" style="top:385px"></div>
  <div class="nav-group" style="top:392px">Laboratory</div>
  <div class="nav-rule" style="top:416px"></div>
  <div class="nav-group" style="top:423px">Suppliers</div>
  <div class="nav-rule" style="top:448px"></div>
  <div class="nav-group" style="top:455px">Insurance</div>
  <div class="nav-rule" style="top:479px"></div>
  <div class="nav-group" style="top:486px">Reports</div>
  <div class="nav-rule" style="top:510px"></div>
</nav>

<!-- patient search -->
<div class="abs label" style="left:252px;top:115px">Patient Searching Field</div>
<div class="abs field" style="left:252px;top:146px;width:299px;height:37px">
  <svg width="16" height="11" viewBox="0 0 16 11"><path d="M2 2l6 6 6-6" fill="none" stroke="var(--blue)" stroke-width="2.4" stroke-linecap="round" stroke-linejoin="round"/></svg>
</div>

<div class="abs patient-card">
  <div class="row"><span>000001</span></div>
  <div class="row"><span>A000001(1) MALE</span><span>01 Jan,1988, 22Yr</span></div>
  <div class="row"><span>WONG KA MING</span></div>
  <div class="row"><span>M: 61203457,&nbsp;&nbsp;&nbsp;T: 24518830</span></div>
  <div class="row"><span>28 Jan, 2010</span></div>
</div>

<div class="abs calendar">
  <div class="abs cal-title">March <span class="year">2015</span></div>
  <svg class="abs cal-nav" style="left:233px" width="8" height="11" viewBox="0 0 8 11"><path d="M6 1.5L2 5.5l4 4" fill="none" stroke="#333" stroke-width="1.4"/></svg>
  <svg class="abs cal-nav" style="left:257px" width="8" height="11" viewBox="0 0 8 11"><path d="M2 1.5l4 4-4 4" fill="none" stroke="#333" stroke-width="1.4"/></svg>
  <div class="abs week-band"></div>
  <div class="abs cal-grid">
    <div class="cal-head">CW</div><div class="cal-head">SUN</div><div class="cal-head">MON</div><div class="cal-head">TUE</div><div class="cal-head">WED</div><div class="cal-head">THU</div><div class="cal-head">FRI</div><div class="cal-head">SAT</div>
    <div class="cw">10</div><div class="day">1</div><div class="day">2</div><div class="day">3</div><div class="day">4</div><div class="day">5</div><div class="day">6</div><div class="day">7</div>
    <div class="cw">11</div><div class="day">8</div><div class="day">9</div><div class="day">10</div><div class="day">11</div><div class="day">12</div><div class="day">13</div><div class="day">14</div>
    <div class="cw">12</div><div class="day">15</div><div class="day">16</div><div class="day">17</div><div class="day">18</div><div class="day">19</div><div class="day">20</div><div class="day">21</div>
    <div class="cw now">13</div><div class="day">22</div><div class="day">23</div><div class="day">24</div><div class="day today"><span>25</span></div><div class="day">26</div><div class="day">27</div><div class="day">28</div>
    <div class="cw">14</div><div class="day">29</div><div class="day">30</div><div class="day">31</div><div class="day next">1</div><div class="day next">2</div><div class="day next">3</div><div class="day next">4</div>
    <div class="cw">15</div><div class="day next">5</div><div class="day next">6</div><div class="day next">7</div><div class="day next">8</div><div class="day next">9</div><div class="day next">10</div><div class="day next">11</div>
  </div>
</div>

<div class="abs divider-v"></div>

<!-- appointment form -->
<div class="abs label" style="left:655px;top:116px">Date</div>
<div class="abs field" style="left:654px;top:148px;width:216px;height:37px">29/84/2015
  <svg width="22" height="20" viewBox="0 0 22 20"><rect x="1" y="3" width="20" height="16" rx="1.5" fill="none" stroke="var(--blue)" stroke-width="1.2"/><path d="M1 7h20" stroke="var(--blue)" stroke-width="1.2"/><path d="M6 1v4M16 1v4" stroke="var(--blue)" stroke-width="1.2"/><g fill="var(--blue)"><rect x="4" y="9" width="2" height="2"/><rect x="8" y="9" width="2" height="2"/><rect x="12" y="9" width="2" height="2"/><rect x="16" y="9" width="2" height="2"/><rect x="4" y="13" width="2" height="2"/><rect x="8" y="13" width="2" height="2"/><rect x="12" y="13" width="2" height="2"/><rect x="16" y="13" width="2" height="2"/></g></svg>
</div>
<div class="abs label" style="left:919px;top:121px">Time</div>
<div class="abs field" style="left:917px;top:148px;width:222px;height:37px;padding-left:12px">06:00 PM
  <svg width="16" height="11" viewBox="0 0 16 11"><path d="M2 2l6 6 6-6" fill="none" stroke="var(--blue)" stroke-width="2.4" stroke-linecap="round" stroke-linejoin="round"/></svg>
</div>

<div class="abs label" style="left:655px;top:203px">Clinic</div>
<div class="abs field" style="left:654px;top:230px;width:221px;height:37px">Brightway
  <svg width="16" height="11" viewBox="0 0 16 11"><path d="M2 2l6 6 6-6" fill="none" stroke="var(--blue)" stroke-width="2.4" stroke-linecap="round" stroke-linejoin="round"/></svg>
</div>
<div class="abs label" style="left:919px;top:203px">Doctor</div>
<div class="abs field" style="left:918px;top:230px;width:221px;height:37px;padding-left:12px">Demo
  <svg width="16" height="11" viewBox="0 0 16 11"><path d="M2 2l6 6 6-6" fill="none" stroke="var(--blue)" stroke-width="2.4" stroke-linecap="round" stroke-linejoin="round"/></svg>
</div>

<div class="abs label" style="left:655px;top:286px">Remarks</div>
<div class="abs field" style="left:655px;top:312px;width:307px;height:37px">
  <svg width="16" height="11" viewBox="0 0 16 11"><path d="M2 2l6 6 6-6" fill="none" stroke="var(--blue)" stroke-width="2.4" stroke-linecap="round" stroke-linejoin="round"/></svg>
</div>
<div class="abs label" style="left:998px;top:286px">Duration</div>
<div class="abs field" style="left:998px;top:312px;width:141px;height:37px">
  <svg width="16" height="11" viewBox="0 0 16 11"><path d="M2 2l6 6 6-6" fill="none" stroke="var(--blue)" stroke-width="2.4" stroke-linecap="round" stroke-linejoin="round"/></svg>
</div>

<div class="abs label" style="left:655px;top:365px">Voucher No</div>
<div class="abs field" style="left:655px;top:390px;width:484px;height:38px"></div>

<div class="abs label" style="left:655px;top:447px">Memo</div>
<div class="abs field" style="left:655px;top:473px;width:484px;height:95px"></div>

<!-- queue table -->
<section class="abs queue">
  <div class="queue-head">
    <span class="th" style="left:47px">Patient Code</span>
    <span class="th" style="left:194px">Name</span>
    <span class="th" style="left:371px">Remarks</span>
    <span class="th" style="left:539px">App. Time</span>
    <span class="th" style="left:652px">Arr. Time</span>
    <span class="th" style="left:758px">Voucher No.</span>
    <span class="th" style="left:887px">Bill</span>
  </div>
  <div class="tr" style="top:37px"><span style="left:47px">000346</span><span style="left:194px">Lam Siu Fong</span><span style="left:540px">9:30 AM</span><span style="left:652px">9:30 AM</span></div>
  <div class="tr" style="top:68px"><span style="left:47px">000346</span><span style="left:194px">Lam Siu Fong</span><span style="left:540px">9:30 AM</span><span style="left:652px">9:30 AM</span></div>
  <div class="tr" style="top:99px"><span style="left:47px">000346</span><span style="left:194px">Lam Siu Fong</span><span style="left:540px">9:30 AM</span><span style="left:652px">9:30 AM</span></div>
  <div class="tr" style="top:130px"><span style="left:47px">000346</span><span style="left:194px">Lam Siu Fong</span><span style="left:540px">9:30 AM</span><span style="left:652px">9:30 AM</span></div>
  <div class="tr fade" style="top:163px"><span style="left:47px">000346</span><span style="left:194px">Lam Siu Fong</span><span style="left:540px">9:30 AM</span><span style="left:652px">9:30 AM</span></div>
</section>
<div class="abs scroll-thumb"></div>

<!-- actions -->
<button class="btn" style="left:253px;top:851px;width:92px">Queue</button>
<button class="btn off" style="left:361px;top:851px;width:110px">Remarks</button>
<button class="btn off" style="left:487px;top:851px;width:111px">Finish</button>
<button class="btn off" style="left:614px;top:851px;width:110px">Delete</button>
<button class="btn" style="left:738px;top:851px;width:110px">Save Memo</button>
<button class="btn" style="left:862px;top:851px;width:110px">Show Doc. W</button>
<button class="btn" style="left:985px;top:851px;width:92px">Bill</button>

<button class="btn" style="left:253px;top:900px;width:92px">Perscription</button>
<button class="btn" style="left:361px;top:900px;width:110px">Decument X</button>
<button class="btn" style="left:487px;top:900px;width:111px">Glucose Data H</button>
<button class="btn" style="left:614px;top:900px;width:110px">Print</button>
<button class="btn" style="left:738px;top:900px;width:110px">Main</button>

</body>
</html>
```